KEP Business Card

the business card should be double sided.
Will need to be Korean on one side and english on the other.
it will need to have:

address
website
skype
phone
cell
fax
name
title
email

just put in dummy details to start - i will then give you correct info once we have the format right.

Also - if you feel creative about the logo we are happy to make some amendments to it so it looks right. We are still at early stages with the logo so happy if you have suggestions around the logo concept.
Updates

The deadline for this has been brought forward to Wednesday 11th December. We can not review any designs after this date.

we will need to make a decision by Wednesday 11th December, so please have designs in by this date and not by the deadline set by lumahive

Target Market(s)

large companies, executives

Industry/Entity Type

Business

Colors

Designer to choose colors to be used in the design.

Requirements
Must have
• double sided - english on one side and korean on the other. we will give you korean wording once we have a design we like.

```html
<!DOCTYPE html>
<html lang="en">
<head>
<meta charset="utf-8">
<title>KEP Business Card</title>
<link href="https://fonts.googleapis.com/css2?family=Didact+Gothic&display=swap" rel="stylesheet">
<style>
  :root {
    --page: #ffffff;
    --card-edge: #3a3a3b;
    --card-glow: #8c8c90;
    --ink-light: #ffffff;
    --ink-dark: #141414;
    --divider: #1e1e1e;
  }
  * { margin: 0; padding: 0; box-sizing: border-box; }
  html, body {
    width: 1200px;
    height: 900px;
    overflow: hidden;
    background: var(--page);
    font-family: "Didact Gothic", "Century Gothic", sans-serif;
  }
  .business-card {
    position: absolute;
    left: 180px;
    top: 210px;
    width: 840px;
    height: 480px;
    background: radial-gradient(ellipse 360px 260px at 46% 52%, var(--card-glow) 0%, #5e5e61 45%, var(--card-edge) 100%);
    box-shadow: 0 10px 24px rgba(0,0,0,0.25);
  }
  .brand {
    position: absolute;
    left: 0;
    width: 760px;
    top: 108px;
    text-align: center;
  }
  .brand-name {
    font-size: 44px;
    letter-spacing: 3px;
    color: var(--ink-dark);
    line-height: 1;
  }
  .brand-web {
    margin-top: 22px;
    font-size: 22px;
    letter-spacing: 2px;
    color: var(--ink-dark);
  }
  .holder {
    position: absolute;
    right: 390px;
    top: 318px;
    text-align: right;
    color: var(--ink-light);
    text-shadow: 2px 3px 4px rgba(0,0,0,0.45);
    line-height: 1;
  }
  .holder-name { font-size: 44px; letter-spacing: 1px; }
  .holder-title { font-size: 42px; margin-top: 2px; }
  .divider {
    position: absolute;
    left: 470px;
    top: 298px;
    width: 3px;
    height: 130px;
    background: var(--divider);
    box-shadow: 2px 2px 4px rgba(0,0,0,0.4);
  }
  .contacts {
    position: absolute;
    left: 492px;
    top: 292px;
    list-style: none;
    color: var(--ink-light);
    font-size: 21px;
    line-height: 22px;
    text-shadow: 1px 2px 3px rgba(0,0,0,0.45);
  }
</style>
</head>
<body>
  <section class="business-card">
    <div class="brand">
      <div class="brand-name">KEP</div>
      <div class="brand-web">www.website.com</div>
    </div>
    <div class="holder">
      <div class="holder-name">MARC OLDEN</div>
      <div class="holder-title">director</div>
    </div>
    <div class="divider"></div>
    <ul class="contacts">
      <li>phone: 0000000</li>
      <li>cell: 0000000</li>
      <li>fax: 0000000</li>
      <li>email: mo@kep.com</li>
      <li>skype: kep__</li>
      <li>address: elmstreet 12</li>
    </ul>
  </section>
</body>
</html>
```